The Brightwater Compass Business Card

We need an attractive business card with the logo that we bought from ArtVantly last year.
Our mission is to contribute to change the way today's leaders manage business companies bringing value to the workplace and helping them to build a new model of creating wealth.
Our logo is clear about our values : we seek Positive Change through People and are convinced that the pursuit of individual well-being and the chase of economic results can converge with the right management.
Management Consulting
Corinne Fabrelle
+34 612 98 70 31
corinne.fabrelle@thebrightwatercompass-mail.net
www.thebrightwatercompass-mail.net

```html
<!DOCTYPE html>
<html lang="en">
<head>
<meta charset="utf-8">
<title>The Brightwater Compass – Business Card</title>
<link rel="stylesheet" href="https://fonts.googleapis.com/css2?family=Cinzel:wght@500&family=Open+Sans:wght@400&display=swap">
<style>
  :root {
    --teal-deep: #0b6f6f;
    --teal-mid: #13918f;
    --teal-light: #2aa5a2;
    --teal-ink: #1a7f7e;
    --paper: #ffffff;
    --backdrop: #e9ecec;
  }
  * { box-sizing: border-box; margin: 0; padding: 0; }
  html, body { width: 1200px; height: 852px; overflow: hidden; }
  body { background: var(--backdrop); position: relative; font-family: "Open Sans", Arial, sans-serif; }

  .card {
    position: absolute;
    width: 520px;
    height: 300px;
    border-radius: 16px;
    overflow: hidden;
    box-shadow: 0 10px 24px rgba(0,0,0,.18);
  }

  /* Front */
  .card-front {
    left: 50px; top: 140px;
    background: linear-gradient(135deg, var(--teal-mid) 0%, var(--teal-deep) 100%);
    display: flex; align-items: center; justify-content: center; gap: 14px;
  }
  .brand-dot { width: 14px; height: 14px; border-radius: 50%; background: var(--paper); flex: none; }
  .brand-name {
    font-family: "Cinzel", Georgia, serif;
    font-weight: 500;
    font-size: 27px;
    color: var(--paper);
    letter-spacing: 1px;
    white-space: nowrap;
  }

  /* Back */
  .card-back {
    left: 630px; top: 412px;
    background: linear-gradient(135deg, var(--teal-mid) 0%, var(--teal-deep) 100%);
  }
  .back-shape { position: absolute; inset: 0; }
  .holder { position: absolute; left: 40px; top: 108px; color: var(--paper); }
  .holder-name { font-family: "Cinzel", Georgia, serif; font-weight: 500; font-size: 22px; letter-spacing: .5px; }
  .holder-role { font-size: 11px; margin-top: 4px; }

  .contacts { position: absolute; left: 36px; bottom: 24px; list-style: none; color: var(--paper); font-size: 10.5px; }
  .contacts li { display: flex; align-items: center; gap: 8px; line-height: 17px; }
  .contacts svg { width: 11px; height: 11px; flex: none; }

  .back-brand {
    position: absolute;
    left: 315px; top: 85px;
    width: 250px; height: 130px;
    transform: rotate(90deg);
    display: flex; flex-direction: column; align-items: center; justify-content: center; gap: 6px;
    color: var(--teal-ink);
  }
  .back-brand .brand-name { color: var(--teal-ink); font-size: 22px; }
  .back-brand .brand-sub {
    font-family: "Cinzel", Georgia, serif;
    font-weight: 500;
    font-size: 13px;
    letter-spacing: 6px;
    padding-left: 6px;
    white-space: nowrap;
  }
  .back-brand .brand-dot { background: var(--teal-ink); width: 16px; height: 16px; margin-top: 10px; }
</style>
</head>
<body>
  <section class="card card-front">
    <span class="brand-dot"></span>
    <span class="brand-name">The Brightwater Compass</span>
  </section>

  <section class="card card-back">
    <svg class="back-shape" viewBox="0 0 520 300" preserveAspectRatio="none">
      <path d="M338 0 C302 90 300 200 320 300 L332 300 C312 200 314 90 350 0 Z" fill="var(--teal-light)"/>
      <path d="M356 0 C320 90 318 200 338 300 L520 300 L520 0 Z" fill="var(--paper)"/>
    </svg>

    <div class="holder">
      <div class="holder-name">Corinne Fabrelle</div>
      <div class="holder-role">Managing Director</div>
    </div>

    <ul class="contacts">
      <li>
        <svg viewBox="0 0 12 12"><path d="M2.5 1 L4.5 1 L5.2 3.6 L4 4.6 C4.6 6 5.8 7.3 7.4 8 L8.4 6.8 L11 7.5 L11 9.5 C11 10.3 10.3 11 9.5 11 C5 11 1 7 1 2.5 C1 1.7 1.7 1 2.5 1 Z" fill="currentColor"/></svg>
        +34 612 98 70 31
      </li>
      <li>
        <svg viewBox="0 0 12 12" fill="none" stroke="currentColor" stroke-width="1"><circle cx="6" cy="6" r="5"/><ellipse cx="6" cy="6" rx="2.2" ry="5"/><path d="M1 6 H11"/></svg>
        www.thebrightwatercompass-mail.net
      </li>
      <li>
        <svg viewBox="0 0 12 12" fill="none" stroke="currentColor" stroke-width="1"><rect x="1" y="2.5" width="10" height="7"/><path d="M1 2.5 L6 6.5 L11 2.5"/></svg>
        corinne.fabrelle@thebrightwatercompass-mail.net
      </li>
    </ul>

    <div class="back-brand">
      <span class="brand-name">The Brightwater</span>
      <span class="brand-sub">Compass</span>
      <span class="brand-dot"></span>
    </div>
  </section>
</body>
</html>
```